Visitenkarten-Design für  Softwareunternehmen
Visitenkarten-Design für Softwareunternehmen
Zielgruppe
Wir sind ein B2B Softwareunternehmen, das eine Energiemonitoringsoftware für die mittelständische Industrie entwickelt hat. Das heißt unsere Visitenkarten werden überwiegend an unsere Zielgruppe, d.h. Geschäftsführer produzierender mittelständischer Industrie ausgehändigt.
Aufgabenstellung
Gleichzeitig treten wir nach außen jung, innovativ und voller Tatendrang auf. Ganz nach unserer Vision: Voll Energie. Null Emission. (Auch gerne auf der Visitenkarte mit aufnehmen). Uns ist es wichtig, unser CI nach außen zu kommunizieren und unsere Webseite auf der Visitenkarte zu platzieren.
Die Visitenkarte soll einzeln für jeden MitarbeiterIn personalisiert werden können.

```html
<!DOCTYPE html>
<html lang="de">
<head>
<meta charset="utf-8">
<title>Visitenkarte VOLTARO</title>
<link rel="stylesheet" href="https://fonts.googleapis.com/css2?family=Didact+Gothic&display=swap">
<style>
  :root {
    --page-bg: #d6d6d6;
    --card-bg: #f4f4f4;
    --band: #2f3b3c;
    --band-text: #ffffff;
    --ink: #222425;
  }
  html, body {
    margin: 0;
    padding: 0;
    width: 1200px;
    height: 848px;
    overflow: hidden;
    background: var(--page-bg);
  }
  .canvas {
    position: relative;
    width: 1200px;
    height: 848px;
  }
  .business-card {
    position: absolute;
    left: 391px;
    top: 102px;
    width: 418px;
    height: 643px;
    background: var(--card-bg);
    font-family: "Didact Gothic", "Helvetica Neue", Arial, sans-serif;
    color: var(--ink);
    text-transform: uppercase;
    text-align: center;
  }
  .brand-band {
    height: 139px;
    background: var(--band);
    display: flex;
    align-items: center;
    justify-content: center;
  }
  .brand-name {
    color: var(--band-text);
    font-size: 62px;
    letter-spacing: 10px;
    line-height: 1;
    margin: 0;
    font-weight: 400;
  }
  .person {
    position: absolute;
    top: 303px;
    left: 0;
    right: 0;
    margin: 0;
    font-size: 19px;
    line-height: 29px;
  }
  .contact {
    position: absolute;
    top: 418px;
    left: 0;
    right: 0;
    margin: 0;
    font-style: normal;
    font-size: 19px;
    line-height: 29px;
  }
  .contact span, .person span { display: block; }
</style>
</head>
<body>
  <main class="canvas">
    <article class="business-card">
      <header class="brand-band">
        <h1 class="brand-name">VOLTARO</h1>
      </header>
      <p class="person">
        <span class="person-name">Maximilian Mustermann</span>
        <span class="person-role">Geschäftsführer</span>
      </p>
      <address class="contact">
        <span>Musterstrasse 234</span>
        <span>34564 Musterhausen am Inn</span>
        <span>Telefon 0481 23 90 57 16</span>
        <span>Mail: info@voltaro.com</span>
        <span>www.voltaro.com</span>
      </address>
    </article>
  </main>
</body>
</html>
```